Outpatient Mental Health Clinic needs a good brochure

We are an outpatient clinic in Michigan, USA and provide therapy and evaluation services for adults, adolescents, and children. Our psychologists, social workers, and counselors help individuals who present with a host of psychological difficulties. Our goal for the brochure is to give an overview of our services so that our marketing person can pass them out to physicians and other referral sources.

Target Market(s)

Our target market are patients who are seeking referrals through their primary care physicians.

Industry/Entity Type

Clinic

Font styles to use
Serif
Sans Serif

Colors
fbf289
f68d4c
f37122
ffffff

Requirements
Must have
• My project must be illustrative enough to show what services are provided. Pictures of individuals is also important.
Nice to have
• In addition to content I would like to have pictures of individuals.

```html
<!DOCTYPE html>
<html lang="en">
<head>
<meta charset="utf-8">
<title>Clinic Trifold Brochure</title>
<link href="https://fonts.googleapis.com/css2?family=Oswald:wght@600&family=Noto+Sans:wght@400;700&family=Ubuntu:wght@700&family=Great+Vibes&display=swap" rel="stylesheet">
<style>
  :root{
    --bg:#c2beba;
    --paper:#ffffff;
    --ink:#3c3a40;
    --plum:#4f4a5e;
    --rose:#ec6f78;
    --cream:#efe4d2;
    --photo-warm:#d9b79a;
    --photo-cool:#a9b9d2;
  }
  *{box-sizing:border-box;margin:0;padding:0}
  html,body{width:1200px;height:1200px;overflow:hidden;background:var(--bg)}
  .brochure{
    position:absolute;left:30px;top:160px;width:1140px;height:880px;
    display:flex;box-shadow:0 30px 60px rgba(0,0,0,.25);
  }
  .panel{position:relative;width:380px;height:880px;background:var(--paper);overflow:hidden}
  .panel--inner-left{border-right:1px solid #eee}
  .panel--inner-mid{border-right:1px solid #eee}
  .heading{
    font-family:"Oswald",sans-serif;font-weight:600;color:var(--rose);
    font-size:26px;letter-spacing:.5px;line-height:1.1;margin:0 0 8px;
  }
  .body-copy{
    font-family:"Noto Sans",sans-serif;font-size:12.5px;line-height:1.42;color:var(--ink);
    margin-bottom:16px;
  }
  .panel--inner-left .content{position:relative;z-index:1;padding:56px 34px 0 34px}
  .panel--inner-left .heading{margin-top:14px}
  .nurse-photo{
    position:absolute;left:0;right:0;bottom:0;height:300px;
    background:linear-gradient(180deg,rgba(255,255,255,1) 0%,rgba(240,226,200,.8) 18%,var(--photo-cool) 55%,var(--photo-warm) 100%);
  }
  .panel--inner-mid .content{padding:40px 34px 0 36px}
  .panel--inner-mid .heading{margin-top:22px}
  .contact{
    position:absolute;left:36px;right:36px;top:690px;
    border:1.5px solid var(--rose);border-radius:14px;padding:30px 26px 14px 26px;
  }
  .contact__title{
    position:absolute;top:-14px;left:50%;transform:translateX(-40%);
    background:var(--plum);color:#fff;font-family:"Noto Sans",sans-serif;font-weight:700;
    font-size:17px;padding:2px 16px;
  }
  .contact__row{display:flex;align-items:center;gap:10px;font-family:"Noto Sans",sans-serif;font-size:14.5px;color:var(--ink);line-height:1.6}
  .contact__row svg{width:13px;height:13px;flex:none}
  .contact__row--plain{padding-left:23px}
  .panel--cover{background:var(--cream)}
  .cover-photo{
    position:absolute;left:0;right:0;top:160px;height:560px;
    background:linear-gradient(120deg,var(--cream) 0%,#e8d8c4 35%,#d98a8f 75%,#c8b8b0 100%);
  }
  .cover-shapes{position:absolute;inset:0}
  .clinic-name{
    position:absolute;left:28px;top:42px;font-family:"Ubuntu",sans-serif;font-weight:700;
    color:#fff;font-size:58px;line-height:.88;letter-spacing:-1px;
  }
  .tagline{
    position:absolute;right:26px;top:728px;text-align:right;font-family:"Great Vibes",cursive;
    color:#fff;font-size:25px;line-height:1.15;
  }
  .logo-name{
    position:absolute;left:36px;bottom:24px;font-family:"Ubuntu",sans-serif;font-weight:700;
    color:#fff;font-size:32px;
  }
</style>
</head>
<body>
<div class="brochure">

  <section class="panel panel--inner-left">
    <div class="nurse-photo" role="img" aria-label="Photo of a nurse giving a patient an injection"></div>
    <div class="content">
      <h2 class="heading">HEADING</h2>
      <p class="body-copy">vitaes ditas nusam eum sitas andestibus magnimped-it a comnis alit ilitatiat andit evellabore et fuga. Ovid maximil laborumque dolut auta nullore henimusdam eost, ulligna tibusa quodit, ni dellent veliquo tem ea vit hictatenti blacess imuscii strumque maio</p>
      <p class="body-copy">Ihiliassunt quia quia volestotatem fuga. Berovit ate-moll atusam fugit am voluptas assinctiis modi seque venitatur? Ribus, cullab ium que volut labora dellessit, sequi doluptaquis et dis dolupta se sit, sin ratetur sit od qui di intur rerrore icabo. Nam, consequ iasit, asperume pa dem rehendi gnatet, cum dolo everrum endiciis mi, quia custi cor sit de ma consera tatemo-lupta aut de quia eost fuga. Icime et optio beatet fugit autectur, coraecto dolest voluptat.</p>
      <h2 class="heading">HEADING</h2>
      <p class="body-copy">Dolestionet faccus repreptur mintio to dollent, quiam, sim quas voloreris ea quas serspis asit, sequi con-sendis isci torpor sequia ipid molo est aut minum</p>
    </div>
  </section>

  <section class="panel panel--inner-mid">
    <div class="content">
      <p class="body-copy">impor re am quis essin nis dereped mosam hilit aut quo blabori tiorem. Debit veribus et ut quo vidusdam fugit facepudi alit, con cuptatempor molo ea dollicip-sus solorio omnis ut asint mo optas simenimpor ma dolore vel inctorrum qui repersp editati oremque eosto torrumq uisque volorpo rrovidus nem quae parum ne et auditaturest quiam ad que odio. Et et, expland aecti-aesti comnienducid quiam la cus alique solupissit ea as ipsum re porpore ssequi derumet, sam, si voluptis exeruptaque doleser rumqui unt.</p>
      <h2 class="heading">HEADING</h2>
      <p class="body-copy">vitaes ditas nusam eum sitas andestibus magnimped-it a comnis alit ilitatiat andit evellabore et fuga. Ovid maximil laborumque dolut auta nullore henimusdam eost, ulligna tibusa quodit, ni dellent veliquo tem ea vit hictatenti blacess imuscii strumque maio</p>
      <p class="body-copy">Ihiliassunt quia quia volestotatem fuga. Berovit ate-moll atusam fugit am voluptas assinctiis modi seque venitatur? Ribus, cullab ium que volut labora dellessit, sequi doluptaquis et dis dolupta se sit, sin ratetur sit od qui di intur rerrore icabo. Nam, consequ iasit, asperume pa dem rehendi gnatet, cum dolo everrum endiciis mi, quia custi cor sit de ma consera tatemo-lupta aut de quia eost fuga. Icime et optio beatet fugit autectur, coraecto dolest voluptat.</p>
    </div>
    <div class="contact">
      <div class="contact__title">Contact Us</div>
      <div class="contact__row contact__row--plain">Address</div>
      <div class="contact__row">
        <svg viewBox="0 0 12 12"><path d="M6 0.5a4 4 0 0 1 4 4c0 3-4 7-4 7s-4-4-4-7a4 4 0 0 1 4-4z" fill="#ec6f78"/><circle cx="6" cy="4.5" r="1.5" fill="#fff"/></svg>
        Michigan, USA
      </div>
      <div class="contact__row">
        <svg viewBox="0 0 12 12"><circle cx="6" cy="6" r="5.3" fill="none" stroke="#ec6f78" stroke-width="1"/><path d="M4 3.2l1.2 1.4-.6.8c.4.9 1.1 1.6 2 2l.8-.6 1.4 1.2-.7 1c-2.4-.3-4.4-2.3-4.7-4.7z" fill="#ec6f78"/></svg>
        +123456789
      </div>
      <div class="contact__row">
        <svg viewBox="0 0 12 12"><rect x="0.5" y="2" width="11" height="8" fill="#ec6f78"/><path d="M0.5 2l5.5 4.5L11.5 2" fill="none" stroke="#fff" stroke-width="1"/></svg>
        emailid@email.com
      </div>
      <div class="contact__row">
        <svg viewBox="0 0 12 12"><g fill="none" stroke="#ec6f78" stroke-width="1"><circle cx="6" cy="6" r="5"/><ellipse cx="6" cy="6" rx="2.2" ry="5"/><path d="M1 6h10M1.8 3.5h8.4M1.8 8.5h8.4"/></g></svg>
        www.websitename.com
      </div>
    </div>
  </section>

  <section class="panel panel--cover">
    <div class="cover-photo" role="img" aria-label="Photo of a doctor in a white coat reading a booklet with a young patient"></div>
    <svg class="cover-shapes" viewBox="0 0 380 880" aria-hidden="true">
      <path d="M0 0H380V150C300 215 140 225 0 150Z" fill="#ec6f78"/>
      <path d="M0 0H380V100C300 175 140 185 0 140Z" fill="#4f4a5e"/>
      <path d="M0 730C110 650 280 640 380 700V880H0Z" fill="#ec6f78"/>
      <path d="M0 780C60 730 180 720 380 720V880H0Z" fill="#4f4a5e"/>
    </svg>
    <div class="clinic-name">clinic<br>name</div>
    <p class="tagline">For patients who are<br>seeking referrals through<br>their primary care physicians</p>
    <div class="logo-name">logo</div>
  </section>

</div>
</body>
</html>
```